Golden Pantry Spice

Distributor of seasonings and spices to the restaurant industry.

Industry/Entity Type

Restaurant

Contact Information for Business Card

Golden Pantry
Derek Hollings
TW Brandvik Distributor
316-487-9021
derek@goldpantryspicehub.com

No minimum order
Gluten & MSG free soup bases

```html
<!DOCTYPE html>
<html lang="en">
<head>
<meta charset="utf-8">
<title>Golden Pantry Spice — Business Card</title>
<link href="https://fonts.googleapis.com/css2?family=Montserrat:wght@500;600&display=swap" rel="stylesheet">
<style>
  :root {
    --backdrop: #e4e4e2;
    --card: #ffffff;
    --ink: #3b3737;
    --rule: #4a3f3f;
    --accent-red: #c8201e;
    --stripe-yellow: #f7d500;
    --stripe-red: #e0321c;
    --stripe-dark: #4b3b37;
  }
  * { margin: 0; padding: 0; box-sizing: border-box; }
  html, body { width: 1200px; height: 900px; overflow: hidden; }
  body {
    background: var(--backdrop);
    font-family: "Montserrat", Arial, sans-serif;
    color: var(--ink);
  }
  .business-card {
    position: absolute;
    left: 150px; top: 193px;
    width: 900px; height: 514px;
    background: var(--card);
    box-shadow: 0 10px 30px rgba(0,0,0,0.15);
  }
  .brand {
    position: absolute;
    left: 250px; top: 118px;
    display: flex; align-items: center; gap: 14px;
  }
  .brand-dot {
    width: 30px; height: 30px; border-radius: 50%;
    background: var(--stripe-yellow);
  }
  .brand-name {
    font-size: 42px; font-weight: 600; color: var(--ink);
    letter-spacing: 0.5px;
  }
  .rule { position: absolute; height: 2px; background: var(--rule); }
  .rule-top { left: 300px; top: 200px; width: 520px; }
  .rule-left { left: 90px; top: 300px; width: 300px; }
  .contact {
    position: absolute; left: 520px; top: 218px;
    list-style: none; font-size: 20px; font-weight: 500;
  }
  .contact li { display: flex; align-items: center; gap: 12px; height: 34px; }
  .contact .email { font-size: 17px; }
  .contact svg { width: 18px; height: 18px; flex: none; }
  .people {
    position: absolute; left: 100px; top: 318px;
    font-size: 21px; font-weight: 500; text-transform: uppercase; line-height: 30px;
  }
  .role { font-size: 16px; font-weight: 600; margin-top: 14px; text-transform: none; }
  .tagline {
    position: absolute; left: 380px; top: 338px; width: 420px;
    text-align: center; color: var(--accent-red);
    font-size: 23px; font-weight: 500; line-height: 42px;
  }
  .stripes { position: absolute; left: 0; right: 0; bottom: 14px; }
  .stripes div { height: 9px; }
  .stripe-yellow { background: var(--stripe-yellow); }
  .stripe-red { background: var(--stripe-red); }
  .stripe-dark { background: var(--stripe-dark); }
</style>
</head>
<body>
  <main class="business-card">
    <div class="brand">
      <span class="brand-dot"></span>
      <span class="brand-name">Golden Pantry Spice</span>
    </div>
    <div class="rule rule-top"></div>

    <ul class="contact">
      <li>
        <svg viewBox="0 0 24 24" aria-hidden="true"><path fill="#c8201e" d="M6.6 10.8a15.1 15.1 0 0 0 6.6 6.6l2.2-2.2a1 1 0 0 1 1-.25 11.4 11.4 0 0 0 3.6.57 1 1 0 0 1 1 1V20a1 1 0 0 1-1 1A17 17 0 0 1 3 4a1 1 0 0 1 1-1h3.5a1 1 0 0 1 1 1c0 1.25.2 2.45.57 3.57a1 1 0 0 1-.25 1z"/></svg>
        <span>316-487-9021</span>
      </li>
      <li class="email">
        <svg viewBox="0 0 24 24" aria-hidden="true"><path fill="#c8201e" d="M2 5h20v14H2z"/><path fill="none" stroke="#fff" stroke-width="1.6" d="M2.5 5.5 12 13l9.5-7.5"/></svg>
        <span>derek@goldpantryspicehub.com</span>
      </li>
    </ul>

    <div class="rule rule-left"></div>
    <div class="people">
      <p>Derek Hollings</p>
      <p>TW Brandvik</p>
      <p class="role">Distributor</p>
    </div>

    <div class="tagline">
      <p>No minimum order</p>
      <p>Gluten &amp; MSG free soup bases</p>
    </div>

    <div class="stripes">
      <div class="stripe-yellow"></div>
      <div class="stripe-red"></div>
      <div class="stripe-dark"></div>
    </div>
  </main>
</body>
</html>
```